Medical Centre Trifold Brochure

New Medical Centre needs a bright and airy Trifold brochure. We want to introduce our practice to the surrounding area so want to advise our services and introduce the Doctors and Nurses.

I will upload all the pictures and logos, along with some pdf pages of styles that we like (and some we dont) to assist your creativity.

We will provide as much feedback for you as possible.

After this project, we would like to work with the same designer to expand into some other brochures etc that we have in mind, so this is a starting point.

Hi Designers,

We are looking forward to seeing yuor work. Are you happy that you have enough information to get started?

Please let me know if you need anything else?

Cheers

Hi Designers.. I should mention the brochure itself.. we are looking for a doubled sided, full colour brochure that will be folded into thirds so it becomes a DL size.. I hope that makes sense.

Any questions always welcome.

Target Market(s)

Females - Mothers / Wives / Grandmothers

Industry/Entity Type

Medical

Requirements
Must have
• Tri Fold Medical – Larkvale Family Health

• Include images of the Doctors (I will supply) and the Nursing Staff

• “Chunks” of information
o Introduction to who we are (I will supply)
o Our services (I will supply)
o Fee’s
• We are a newly renovated Medical Clinic
• Plotwise Map of our location – Photo of the outside of the centre near the plotwise map
• Opening Hours
• Contact Details / website address www.larkvalefamilyhealth.com.au (not yet live but must be included)
• Interior Reception area photo
• Ask a question.. “Are you worried about your patient history?.. We can help”
• Need to leave a space for a Magnet.. (business card sized)

3 Doctor Photos (2 uploaded already)
Image of the centre (uploaded already)

I will upload a detailed description of what we are looking for.
Nice to have
• Photo's of 2 Nurses (1 already uploaded - Maren)

```html
<!DOCTYPE html>
<html lang="en">
<head>
<meta charset="utf-8">
<title>Larkvale Family Health – Trifold Brochure</title>
<link rel="stylesheet" href="https://fonts.googleapis.com/css2?family=Didact+Gothic&family=Arimo:wght@400;700&display=swap">
<style>
  :root {
    --green: #8cc63f;
    --green-dark: #6aa82a;
    --green-pale: #dcedc4;
    --ink: #4a4a4a;
    --ink-soft: #666;
    --orange: #f29a1f;
    --paper: #ffffff;
    --backdrop: #eceee8;
    --head-font: "Didact Gothic", "Century Gothic", sans-serif;
    --body-font: "Arimo", Arial, sans-serif;
  }
  * { box-sizing: border-box; margin: 0; padding: 0; }
  html, body { width: 900px; height: 1200px; overflow: hidden; }
  body { background: var(--backdrop); position: relative; font-family: var(--body-font); color: var(--ink); }

  .sheet {
    position: absolute; left: 50px; width: 800px; height: 564px;
    background: var(--paper); overflow: hidden;
    box-shadow: 0 2px 10px rgba(0,0,0,.15);
  }
  .sheet--outside { top: 24px; }
  .sheet--inside { top: 612px; }
  .abs { position: absolute; }
  .photo { position: absolute; }
  .wave { position: absolute; left: 0; top: 0; width: 800px; height: 564px; pointer-events: none; }

  /* outside */
  .photo--centre { left: 0; top: 0; width: 620px; height: 175px; background: linear-gradient(180deg, #c9d3dc 0%, #a86e55 55%, #8a5a44 100%); }
  .brand { left: 600px; top: 60px; width: 190px; display: flex; align-items: center; gap: 8px; }
  .brand__mark { width: 14px; height: 14px; border-radius: 50%; background: var(--green); flex: none; }
  .brand__name { font-family: var(--head-font); color: var(--green-dark); font-size: 19px; line-height: 1.1; }

  .section-title { font-family: var(--head-font); font-weight: 400; color: var(--ink); }
  .team-title { left: 21px; top: 160px; font-size: 22px; }
  .hours-title { left: 300px; top: 160px; font-size: 22px; }
  .position-title { left: 300px; top: 238px; font-size: 22px; }

  .doctor { position: absolute; left: 26px; width: 219px; height: 84px; background: var(--green); border-radius: 8px; }
  .doctor__photo { position: absolute; left: -4px; top: 8px; width: 66px; height: 70px; background: linear-gradient(180deg, #d7dde0, #b7a594); border: 2px solid #fff; }
  .doctor__name { position: absolute; left: 74px; top: 6px; font-family: var(--head-font); color: #fff; font-size: 16px; }
  .doctor__bio { position: absolute; left: 74px; top: 28px; right: 8px; color: #fff; font-size: 7.5px; line-height: 1.3; }

  .hours { left: 300px; top: 194px; font-size: 11px; line-height: 1.55; color: var(--ink); }
  .photo--map { left: 300px; top: 272px; width: 165px; height: 96px; background: linear-gradient(135deg, #eceae4, #dfe3d6); border: 1px solid #ddd; }
  .contact { left: 300px; top: 392px; font-size: 10px; line-height: 1.5; color: var(--ink); }

  .tagline { left: 520px; top: 186px; width: 258px; text-align: right; font-family: var(--head-font); color: var(--green-dark); font-size: 16px; line-height: 1.3; }
  .photo--family { left: 530px; top: 236px; width: 270px; height: 265px; background: linear-gradient(160deg, #e8eef4 0%, #cfd9e3 60%, #b8c6d4 100%); }
  .site-url { right: 14px; bottom: 10px; font-size: 11px; color: var(--ink-soft); }
  .site-url b { color: var(--ink); }

  /* inside */
  .photo--reception { left: 0; top: 0; width: 262px; height: 150px; background: linear-gradient(160deg, #eae6df, #c9c0b3); }
  .photo--beach { left: 265px; top: 0; width: 265px; height: 150px; background: linear-gradient(180deg, #3b8fd6 0%, #7fc0ee 60%, #e7d9b0 100%); }
  .photo--outing { left: 533px; top: 0; width: 267px; height: 150px; background: linear-gradient(180deg, #cfe0ee 0%, #aebfd0 60%, #8fa06a 100%); }
  .panel-title { top: 184px; font-size: 26px; }
  .about-title { left: 24px; }
  .services-title { left: 287px; }
  .fees-title { left: 550px; top: 174px; }
  .copy { font-size: 10.5px; line-height: 1.38; color: var(--ink-soft); }
  .about-copy { left: 24px; top: 224px; width: 238px; }
  .services-copy { left: 287px; top: 224px; width: 238px; }
  .fees-copy { left: 550px; top: 204px; width: 236px; }
  .service-list { left: 287px; top: 282px; list-style: none; font-size: 10.5px; line-height: 1.4; color: var(--ink-soft); }
  .service-list li { position: relative; padding-left: 14px; }
  .service-list li::before { content: ""; position: absolute; left: 0; top: 3px; border-left: 8px solid var(--orange); border-top: 4.5px solid transparent; border-bottom: 4.5px solid transparent; }
  .photo--team { left: 0; top: 395px; width: 262px; height: 169px; background: linear-gradient(180deg, #f4f4f4, #9bb4cf 70%, #3e6fa6 100%); }
  .photo--seniors { left: 320px; top: 410px; width: 200px; height: 154px; background: linear-gradient(180deg, #eef1ea, #c9c1b2 70%, #9c8e7a 100%); }
  .photo--kids { left: 545px; top: 380px; width: 255px; height: 184px; background: linear-gradient(180deg, #f3f3ee, #d99b7f 55%, #5a8bc5 100%); }
</style>
</head>
<body>

<section class="sheet sheet--outside">
  <div class="photo photo--centre" role="img" aria-label="Photo of the renovated medical centre exterior"></div>
  <svg class="wave" viewBox="0 0 800 564" aria-hidden="true">
    <path d="M0 150 C200 185 430 150 640 70 L640 0 L800 0 L800 200 L0 200 Z" fill="#fff"/>
    <path d="M0 150 C200 185 430 150 640 70" fill="none" stroke="var(--green)" stroke-width="5"/>
  </svg>

  <div class="brand abs">
    <span class="brand__mark"></span>
    <span class="brand__name">Larkvale Family Health</span>
  </div>

  <h2 class="section-title team-title abs">Our Team</h2>
  <div class="doctor" style="top:196px">
    <div class="doctor__photo" role="img" aria-label="Portrait of Dr. Corinne"></div>
    <div class="doctor__name">Dr. Corinne</div>
    <p class="doctor__bio">Lorem ipsum dolor sit amet, consectetur adipisicing elit, sed do eiusmod tempor incididunt ut labore et dolore magna aliqua. Ut enim ad minim veniam, quis nostrud exercitation.</p>
  </div>
  <div class="doctor" style="top:303px">
    <div class="doctor__photo" role="img" aria-label="Portrait of Dr. Maren"></div>
    <div class="doctor__name">Dr. Maren</div>
    <p class="doctor__bio">Lorem ipsum dolor sit amet, consectetur adipisicing elit, sed do eiusmod tempor incididunt ut labore et dolore magna aliqua. Ut enim ad minim veniam, quis nostrud exercitation.</p>
  </div>
  <div class="doctor" style="top:410px">
    <div class="doctor__photo" role="img" aria-label="Portrait of Dr. Owen Hartley"></div>
    <div class="doctor__name">Dr. Owen Hartley</div>
    <p class="doctor__bio">Lorem ipsum dolor sit amet, consectetur adipisicing elit, sed do eiusmod tempor incididunt ut labore et dolore magna aliqua. Ut enim ad minim veniam, quis nostrud exercitation.</p>
  </div>

  <h2 class="section-title hours-title abs">Opening Hour</h2>
  <p class="hours abs">Mon - Fri : 08.00AM - 08.00PM<br>Sat - Sun : 10.00AM - 10.30PM</p>
  <h2 class="section-title position-title abs">POSITION</h2>
  <div class="photo photo--map" role="img" aria-label="Plotwise map of the centre location"></div>
  <p class="contact abs">1/ 48 Fernbrook Rd, Larkvale<br>SA 5999, Australia<br>P : (08) 5550 1441<br>F : (08) 5550 1434<br>E : info@larkvalefamilyhealth.com.au<br>www.larkvalefamilyhealth.com.au</p>

  <p class="tagline abs">Lorem ipsum dolor<br>consectetur adipisicing</p>
  <div class="photo photo--family" role="img" aria-label="Photo of a smiling family"></div>

  <svg class="wave" viewBox="0 0 800 564" aria-hidden="true">
    <path d="M0 478 C260 548 560 520 800 462 L800 480 C560 548 260 560 0 500 Z" fill="var(--green)"/>
    <path d="M0 500 C260 560 560 548 800 480 L800 564 L0 564 Z" fill="#fff"/>
  </svg>
  <p class="site-url abs">www.<b>larkvalefamilyhealth</b>.com.au</p>
</section>

<section class="sheet sheet--inside">
  <div class="photo photo--reception" role="img" aria-label="Photo of a smiling receptionist at the front desk"></div>
  <div class="photo photo--beach" role="img" aria-label="Photo of children playing on the beach"></div>
  <div class="photo photo--outing" role="img" aria-label="Photo of a family outing by the car"></div>
  <svg class="wave" viewBox="0 0 800 564" aria-hidden="true">
    <path d="M0 130 C200 165 420 90 620 100 C700 104 760 120 800 128 L800 170 L0 170 Z" fill="#fff"/>
    <path d="M0 130 C200 165 420 90 620 100 C700 104 760 120 800 128" fill="none" stroke="var(--green)" stroke-width="5"/>
  </svg>

  <h2 class="section-title panel-title about-title abs">ABOUT US</h2>
  <p class="copy about-copy abs">Lorem ipsum dolor sit amet, consectetur adipisicing elit, sed do eiusmod tempor incididunt ut labore et dolore magna aliqua. Ut enim ad minim veniam, quis nostrud exercitation ullamco laboris nisi ut aliquip ex ea commodo consequat. Duis aute irure dolor in reprehenderit in voluptate velit esse cillum dolore eu fugiat nulla pariatur. Excepteur sint occaecat cupidatat non proident,</p>

  <h2 class="section-title panel-title services-title abs">SERVICES</h2>
  <p class="copy services-copy abs">Lorem ipsum dolor sit amet, consectetur adipisicing elit, sed do eiusmod tempor incididunt ut labore et dolore</p>
  <ul class="service-list abs">
    <li>Medical – Larkvale Family Health</li>
    <li>Dental – Larkvale Family Dental</li>
    <li>Physiotherapy (we say "Physio")</li>
    <li>Podiatry</li>
    <li>Psychology</li>
    <li>Dieticians</li>
  </ul>

  <h2 class="section-title panel-title fees-title abs">FEE'S</h2>
  <p class="copy fees-copy abs">Lorem ipsum dolor sit amet, consectetur adipisicing elit, sed do eiusmod tempor incididunt ut labore et dolore magna aliqua. Ut enim ad minim veniam, quis nostrud exercitation ullamco laboris nisi ut aliquip ex ea commodo consequat. Duis aute irure dolor in reprehenderit in voluptate velit esse cillum dolore eu fugiat nulla pariatur. Excepteur sint occaecat cupidatat non proident, sunt in culpa qui officia deserunt mollit anim id est laborum</p>

  <div class="photo photo--team" role="img" aria-label="Photo of the doctors and nursing staff"></div>
  <div class="photo photo--seniors" role="img" aria-label="Photo of a smiling older couple"></div>
  <div class="photo photo--kids" role="img" aria-label="Photo of a group of teenagers"></div>
  <svg class="wave" viewBox="0 0 800 564" aria-hidden="true">
    <path d="M0 400 C90 380 180 392 262 420 L262 395 L0 395 Z" fill="#fff"/>
    <path d="M0 400 C90 380 180 392 262 420" fill="none" stroke="var(--green)" stroke-width="3"/>
    <path d="M320 430 C380 400 460 400 520 418 L520 405 L320 405 Z" fill="#fff"/>
    <path d="M320 430 C380 400 460 400 520 418" fill="none" stroke="var(--green)" stroke-width="3"/>
    <path d="M545 395 C630 370 720 372 800 390 L800 375 L545 375 Z" fill="#fff"/>
    <path d="M545 395 C630 370 720 372 800 390" fill="none" stroke="var(--green)" stroke-width="3"/>
  </svg>
</section>

</body>
</html>
```